Business Card Design

I need a business card for a new company based in Australia called "MedLinkora".

Its a cloud program for GPs that allows them to search for the specialist they require using a simple user friendly tool.

I would like the colours to match those in the program (the colours in the logo attached).

The final design should reflect the programs clarity, ease of use and professionalism.

Target Market(s)

GPs and other Health Professionals

Industry/Entity Type

Business

Contact Information for Business Card

MedLinkora; The Trusted Clinician Index; Marla Ostrove CEO; 0438215906; marla@medlinkora.example; www.medlinkora.example

Requirements
Must have
• Must have the logo attached; the web address and my name and phone number
Nice to have
• the slogan "The Trusted Clinician Index"

```html
<!DOCTYPE html>
<html lang="en">
<head>
<meta charset="utf-8">
<title>MedLinkora Business Card</title>
<link rel="stylesheet" href="https://fonts.googleapis.com/css2?family=Questrial&family=Open+Sans:wght@700&display=swap">
<style>
  :root {
    --backdrop: #ebecec;
    --card: #ffffff;
    --brand-blue: #0cb1e3;
    --brand-grey: #b3b4b5;
    --tagline-grey: #a2a4a6;
    --ink: #2b2b2b;
  }
  * { margin: 0; padding: 0; box-sizing: border-box; }
  html, body {
    width: 995px;
    height: 1200px;
    overflow: hidden;
    background: var(--backdrop);
  }
  .canvas {
    position: relative;
    width: 995px;
    height: 1200px;
  }
  .card {
    position: absolute;
    width: 816px;
    height: 481px;
    background: var(--card);
  }
  .card--front { left: 86px; top: 73px; }
  .card--back  { left: 78px; top: 627px; }
  .card__bands {
    position: absolute;
    inset: 0;
    width: 100%;
    height: 100%;
  }
  .band--blue { fill: var(--brand-blue); }
  .band--grey { fill: var(--brand-grey); }

  .brand {
    position: absolute;
    left: 84px;
    top: 132px;
    display: flex;
    align-items: center;
    gap: 22px;
  }
  .brand__mark {
    width: 64px;
    height: 64px;
    flex: none;
    background: var(--brand-blue);
  }
  .brand__name {
    font-family: "Questrial", sans-serif;
    font-weight: 400;
    font-size: 64px;
    line-height: 1;
    color: var(--ink);
    white-space: nowrap;
  }
  .brand-tagline {
    position: absolute;
    left: 84px;
    top: 240px;
    font-family: "Questrial", sans-serif;
    font-size: 35px;
    line-height: 1;
    letter-spacing: 1.5px;
    color: var(--tagline-grey);
    white-space: nowrap;
  }

  .holder {
    position: absolute;
    left: 118px;
    top: 98px;
    font-family: "Open Sans", sans-serif;
    font-weight: 700;
    font-size: 31px;
    line-height: 1;
    color: var(--ink);
    white-space: nowrap;
  }
  .contact-list {
    position: absolute;
    left: 118px;
    top: 172px;
    list-style: none;
  }
  .contact-list__item {
    display: flex;
    align-items: center;
    height: 40px;
    margin-bottom: 24px;
    font-family: "Questrial", sans-serif;
    font-size: 34px;
    color: var(--ink);
    white-space: nowrap;
  }
  .contact-list__icon {
    width: 26px;
    height: 26px;
    margin-right: 18px;
    flex: none;
    fill: none;
    stroke: var(--brand-blue);
    stroke-width: 1.6;
  }
</style>
</head>
<body>
<main class="canvas">

  <section class="card card--front">
    <svg class="card__bands" viewBox="0 0 719 424" preserveAspectRatio="none" aria-hidden="true">
      <polygon class="band--grey" points="342,363 716,363 716,383 374,383"/>
      <polygon class="band--blue" points="0,351 299,351 365,391 716,391 716,416 0,416"/>
    </svg>
    <div class="brand">
      <span class="brand__mark" aria-hidden="true"></span>
      <h1 class="brand__name">MedLinkora</h1>
    </div>
    <p class="brand-tagline">The Trusted Clinician Index</p>
  </section>

  <section class="card card--back">
    <svg class="card__bands" viewBox="0 0 719 424" preserveAspectRatio="none" aria-hidden="true">
      <polygon class="band--grey" points="3,363 378,363 348,384 3,384"/>
      <polygon class="band--blue" points="3,392 357,392 421,353 719,353 719,417 3,417"/>
    </svg>
    <h2 class="holder">Marla Ostrove CEO</h2>
    <ul class="contact-list">
      <li class="contact-list__item">
        <svg class="contact-list__icon" viewBox="0 0 26 26" aria-hidden="true">
          <rect x="7" y="2" width="12" height="22" rx="2"/>
          <line x1="7" y1="19" x2="19" y2="19"/>
          <line x1="12" y1="21.5" x2="14" y2="21.5"/>
        </svg>
        0438215906
      </li>
      <li class="contact-list__item">
        <svg class="contact-list__icon" viewBox="0 0 26 26" aria-hidden="true">
          <rect x="2" y="6" width="22" height="14" rx="1"/>
          <polyline points="2,6 13,14 24,6"/>
          <line x1="2" y1="20" x2="10" y2="12"/>
          <line x1="24" y1="20" x2="16" y2="12"/>
        </svg>
        marla@medlinkora.example
      </li>
      <li class="contact-list__item">
        <svg class="contact-list__icon" viewBox="0 0 26 26" aria-hidden="true">
          <circle cx="13" cy="13" r="11"/>
          <ellipse cx="13" cy="13" rx="5" ry="11"/>
          <line x1="2" y1="13" x2="24" y2="13"/>
          <line x1="4" y1="7" x2="22" y2="7"/>
          <line x1="4" y1="19" x2="22" y2="19"/>
        </svg>
        www.medlinkora.example
      </li>
    </ul>
  </section>

</main>
</body>
</html>
```